Business Card Design using new attached logo

We are a family run Plumbing and Heating firm looking to improve our company image with an improved business card and new logo.We are looking to keep the company colour (Blue) involved in our design

Reason: New logo added which needs to be incorporated on designs

Industry/Entity Type

Business

Contact Information for Business Card

See attachment of all info required.

Requirements
Must have
• We have just picked a new company logo which is attached.
• Could you please provide your business card designs using this logo.
• We are looking for the logo on the back as well as the front with all the info required

```html
<!DOCTYPE html>
<html lang="en">
<head>
<meta charset="utf-8">
<title>KVT Services Ltd – Business Cards</title>
<link rel="stylesheet" href="https://fonts.googleapis.com/css2?family=Arimo:wght@400&display=swap">
<style>
  :root {
    --brand-blue: #2f52a3;
    --brand-orange: #f05a2c;
    --card-white: #ffffff;
    --stage: #f1f1f1;
    --text-light: #ffffff;
  }
  * { box-sizing: border-box; margin: 0; padding: 0; }
  html, body {
    width: 1200px;
    height: 1001px;
    overflow: hidden;
    background: var(--stage);
    font-family: "Arimo", Arial, sans-serif;
  }
  .stage { position: relative; width: 1200px; height: 1001px; }

  .card {
    position: absolute;
    width: 600px;
    height: 360px;
  }

  /* Company name: one line, one size, one weight */
  .company-name {
    color: var(--brand-blue);
    font-weight: 400;
    white-space: nowrap;
    letter-spacing: 1px;
  }

  /* Front: orange */
  .card-front {
    left: 60px;
    top: 110px;
    background: var(--brand-orange);
  }
  .card-front .company-name {
    position: absolute;
    left: 0; right: 0;
    top: 128px;
    text-align: center;
    font-size: 44px;
    line-height: 50px;
  }

  .services-line {
    position: absolute;
    left: 0; right: 0;
    top: 218px;
    bottom: 0;
    display: flex;
    justify-content: center;
    align-items: stretch;
    color: var(--text-light);
    font-size: 19px;
    letter-spacing: 3px;
  }
  .services-line .service { padding: 8px 16px 0; }
  .services-divider { width: 1px; background: var(--text-light); }

  /* Back: white with blue panel */
  .card-back {
    left: 540px;
    top: 530px;
    background: var(--card-white);
    display: flex;
  }
  .back-panel {
    width: 290px;
    background: var(--brand-blue);
    color: var(--text-light);
    padding: 168px 0 0 54px;
  }
  .holder-name { font-size: 24px; letter-spacing: 0.5px; }
  .holder-role { font-size: 16px; margin-top: 6px; }

  .back-details {
    flex: 1;
    padding: 62px 20px 0 30px;
    color: var(--brand-blue);
  }
  .back-details .company-name {
    font-size: 22px;
    line-height: 28px;
    letter-spacing: 0.5px;
  }

  .address, .contacts {
    font-style: normal;
    font-size: 16px;
    line-height: 22px;
    letter-spacing: 0.2px;
  }
  .address { margin-top: 52px; }
  .contacts { margin-top: 22px; list-style: none; }
</style>
</head>
<body>
<main class="stage">

  <section class="card card-front" aria-label="Business card front">
    <p class="company-name">KVT SERVICES LTD</p>
    <div class="services-line">
      <span class="service">PLUMBING</span>
      <span class="services-divider"></span>
      <span class="service">HEATING</span>
    </div>
  </section>

  <section class="card card-back" aria-label="Business card back">
    <div class="back-panel">
      <p class="holder-name">MARK ELLISON</p>
      <p class="holder-role">DIRECTOR</p>
    </div>
    <div class="back-details">
      <p class="company-name">KVT SERVICES LTD</p>
      <address class="address">
        14 MILL PARADE,<br>
        ELMFIELD ROAD, REDBOURNE,<br>
        SURREY RB2 7KL
      </address>
      <ul class="contacts">
        <li>TEL: 020 7946 0321</li>
        <li>FAX: 020 7946 0874</li>
        <li>MOBILE: 07700 900418</li>
        <li>markellison@kvtservicesltd.co.uk</li>
      </ul>
    </div>
  </section>

</main>
</body>
</html>
```